Varlowe Supply Partners
Business Cards and Stationary
Project: Varlowe Supply Partners
Varlowe Supply Partners -
Creative Brief
Professional
Daniel Varlowe
Manufacturer's Representative
20375 82nd Lane NW Elk Ridge, MN 55492
dvarlowe@varlowesupply-example.com
www.varlowesupply-example.com

```html
<!DOCTYPE html>
<html lang="en">
<head>
<meta charset="utf-8">
<title>Varlowe Supply Partners – Business Card</title>
<link href="https://fonts.googleapis.com/css2?family=Great+Vibes&family=Arimo:wght@400;700&display=swap" rel="stylesheet">
<style>
  :root {
    --stage-light: #6b6b6b;
    --stage-dark: #383838;
    --card-white: #ffffff;
    --card-grey: #dcdcdc;
    --brand-blue: #1f5da8;
    --brand-blue-deep: #0b3c7d;
    --brand-navy: #0a2f66;
    --ink-blue: #1a3f7a;
    --ink-grey: #6d6d6d;
    --accent-sky: #5fa8ec;
  }
  * { margin: 0; padding: 0; box-sizing: border-box; }
  html, body { width: 1200px; height: 901px; overflow: hidden; }
  body {
    position: relative;
    background: radial-gradient(ellipse at 50% 40%, var(--stage-light) 0%, var(--stage-dark) 100%);
    font-family: "Arimo", Arial, sans-serif;
  }
  .card {
    position: absolute;
    border-radius: 15px;
    overflow: hidden;
    box-shadow: 0 4px 14px rgba(0,0,0,0.45);
  }
  .card-front {
    left: 29px; top: 15px; width: 616px; height: 426px;
    background: radial-gradient(ellipse at 62% 35%, var(--card-white) 0%, #f1f1f1 45%, var(--card-grey) 100%);
  }
  .front-band {
    position: absolute; left: 0; top: 212px; width: 51px; height: 173px;
    background: linear-gradient(90deg, var(--brand-blue-deep), var(--brand-blue));
  }
  .front-name {
    position: absolute; right: 40px; top: 22px;
    font-family: "Great Vibes", cursive; font-weight: 400;
    font-size: 60px; line-height: 1; color: var(--brand-navy);
  }
  .front-title {
    position: absolute; right: 44px; top: 94px;
    font-size: 16px; letter-spacing: 0.4px; color: var(--ink-grey);
  }
  .contact {
    position: absolute; left: 78px; top: 226px; width: 500px;
    font-size: 12px;
  }
  .contact-row { position: absolute; left: 0; display: flex; }
  .contact-label { width: 100px; font-weight: 700; color: var(--ink-blue); }
  .contact-value { color: var(--ink-grey); line-height: 1.25; }
  .card-back {
    left: 574px; top: 458px; width: 618px; height: 431px;
    background: radial-gradient(ellipse at 50% 48%, #2d79c8 0%, var(--brand-blue) 35%, var(--brand-blue-deep) 80%, var(--brand-navy) 100%);
  }
  .back-name {
    position: absolute; left: 0; right: 0; top: 166px; text-align: center;
    font-family: "Great Vibes", cursive; font-weight: 400;
    font-size: 72px; line-height: 1; color: var(--card-white);
  }
  .back-title {
    position: absolute; left: 0; right: 0; top: 254px; text-align: center;
    font-size: 13px; letter-spacing: 0.5px; color: var(--accent-sky);
  }
  .back-web {
    position: absolute; left: 0; right: 0; bottom: 12px; text-align: center;
    font-size: 17px; color: var(--accent-sky);
  }
</style>
</head>
<body>
  <section class="card card-front">
    <div class="front-band"></div>
    <h1 class="front-name">Daniel Varlowe</h1>
    <p class="front-title">MANUFACTURER'S REPRESENTATIVE</p>
    <div class="contact">
      <div class="contact-row" style="top:0"><span class="contact-label">ADDRESS</span><span class="contact-value">20375 82ND LANE NW<br>ELK RIDGE, MN 55492</span></div>
      <div class="contact-row" style="top:41px"><span class="contact-label">PHONE</span><span class="contact-value">763.555.0142</span></div>
      <div class="contact-row" style="top:68px"><span class="contact-label">FAX</span><span class="contact-value">763.555.0187</span></div>
      <div class="contact-row" style="top:97px"><span class="contact-label">EMAIL</span><span class="contact-value">dvarlowe@varlowesupply-example.com</span></div>
      <div class="contact-row" style="top:126px"><span class="contact-label">WEB ADDRESS</span><span class="contact-value">www.varlowesupply-example.com</span></div>
    </div>
  </section>

  <section class="card card-back">
    <h2 class="back-name">Daniel Varlowe</h2>
    <p class="back-title">MANUFACTURER'S REPRESENTATIVE</p>
    <p class="back-web">www.varlowesupply-example.com</p>
  </section>
</body>
</html>
```